Ridgeline Sawcutting, Inc. Business Card

Create a business card that is eye catching and based around concrete sawcutting. I've attached our current business card and logo for reference. We like aspects of the current business card, but it is starting to feel very loud and lost. We would like something that is still fun but is more modern and streamlined.

```html
<!DOCTYPE html>
<html lang="en">
<head>
<meta charset="utf-8">
<title>Ridgeline Sawcutting, Inc. Business Card</title>
<link rel="stylesheet" href="https://fonts.googleapis.com/css2?family=Montserrat:wght@400;500;700;800&display=swap">
<style>
  :root {
    --page: #e9e9e9;
    --card-dark: #1d1d1e;
    --plate-light: #4a4a4c;
    --plate-mid: #2c2c2e;
    --plate-dark: #161617;
    --mark-navy: #243a7a;
    --text-main: #f2f2f2;
    --text-soft: #c9c9c9;
    --rule: #8a8a8a;
  }
  * { box-sizing: border-box; margin: 0; padding: 0; }
  html, body { width: 1200px; height: 1200px; overflow: hidden; }
  body {
    background: var(--page);
    font-family: "Montserrat", sans-serif;
    display: flex; align-items: center; justify-content: center; gap: 60px;
  }
  .card {
    position: relative; width: 440px; height: 770px;
    border-radius: 28px; overflow: hidden;
    background: var(--card-dark);
    box-shadow: 0 10px 30px rgba(0,0,0,0.25);
  }
  .card-bg { position: absolute; inset: 0; }
  .plate-fill { fill: url(#plateGradient); }
  .brand-mark {
    position: absolute; left: 50%; transform: translateX(-50%);
    width: 230px; height: 230px; border-radius: 50%;
    background: var(--mark-navy);
    display: flex; align-items: center; justify-content: center;
    text-align: center;
  }
  .brand-name {
    color: var(--text-main); font-weight: 700; font-size: 22px;
    line-height: 1.25; letter-spacing: 1px;
  }
  .front .brand-mark { top: 85px; }
  .contact {
    position: absolute; left: 0; right: 0; top: 355px;
    text-align: center; color: var(--text-main);
  }
  .person-name { font-weight: 800; font-size: 27px; letter-spacing: 1px; }
  .person-role { font-size: 14px; color: var(--text-soft); margin-top: 2px; }
  .icon-row {
    display: flex; align-items: center; justify-content: center; gap: 8px;
    margin: 22px 0 12px;
  }
  .icon-rule { width: 70px; height: 2px; background: var(--rule); margin: 0 10px; }
  .icon-chip { width: 18px; height: 18px; border-radius: 4px; background: var(--text-soft); }
  .contact-lines { font-size: 17px; line-height: 1.5; color: var(--text-soft); }
  .address-rule { width: 60px; height: 2px; background: var(--rule); margin: 16px auto; }
  .address { font-size: 17px; line-height: 1.5; color: var(--text-soft); }
  .back .brand-mark { top: 190px; }
  .services { position: absolute; left: 70px; top: 490px; color: var(--text-main); }
  .services-title { font-weight: 700; font-size: 30px; letter-spacing: 1px; color: #dcdcdc; }
  .services-list { list-style: none; margin-top: 22px; padding-left: 40px; }
  .services-list li {
    font-weight: 700; font-size: 18px; line-height: 1.7; position: relative;
  }
  .services-list li::before {
    content: ""; position: absolute; left: -22px; top: 12px;
    width: 7px; height: 7px; border-radius: 50%; background: var(--text-soft);
  }
</style>
</head>
<body>
  <svg width="0" height="0" style="position:absolute">
    <defs>
      <linearGradient id="plateGradient" x1="0" y1="0" x2="1" y2="1">
        <stop offset="0" stop-color="#1c1c1d"/>
        <stop offset="0.35" stop-color="#4a4a4c"/>
        <stop offset="0.65" stop-color="#2c2c2e"/>
        <stop offset="1" stop-color="#161617"/>
      </linearGradient>
    </defs>
  </svg>

  <section class="card front">
    <svg class="card-bg" viewBox="0 0 440 770" width="440" height="770">
      <rect class="plate-fill" x="0" y="0" width="440" height="770" role="img" aria-label="Diamond tread steel plate texture"/>
      <path d="M0 190 H80 A140 140 0 0 1 360 190 H440 V770 H0 Z" fill="var(--card-dark)"/>
    </svg>
    <div class="brand-mark"><span class="brand-name">RIDGELINE<br>SAWCUTTING</span></div>
    <div class="contact">
      <h1 class="person-name">DANA MORETTI</h1>
      <p class="person-role">Owner</p>
      <div class="icon-row">
        <span class="icon-rule"></span>
        <span class="icon-chip"></span><span class="icon-chip"></span>
        <span class="icon-chip"></span><span class="icon-chip"></span>
        <span class="icon-rule"></span>
      </div>
      <p class="contact-lines">(855) 555-0142<br>855-RDG-CUTS<br>dana@ridgelinesawcutting.com<br>www.ridgelinesawcutting.com</p>
      <div class="address-rule"></div>
      <p class="address">48 Harmon Ridge Road,<br>Millbrook, NJ 07999</p>
    </div>
  </section>

  <section class="card back">
    <svg class="card-bg" viewBox="0 0 440 770" width="440" height="770">
      <rect class="plate-fill" x="0" y="0" width="440" height="770" role="img" aria-label="Diamond tread steel plate texture"/>
    </svg>
    <div class="brand-mark"><span class="brand-name">RIDGELINE<br>SAWCUTTING</span></div>
    <div class="services">
      <h2 class="services-title">OUR SERVICES</h2>
      <ul class="services-list">
        <li>Wall Sawing</li>
        <li>Core Drilling</li>
        <li>Slab Sawing</li>
        <li>Breaking &amp; Removal</li>
      </ul>
    </div>
  </section>
</body>
</html>
```